Construction machinery rental / heavy equipment rental needs a nice billboard

We need a billboard for our company.
We rent out construction machinery such as excavators, wheel loaders, wheel dumpers and so on...

I would like an elegant, simple, dark design.
Colors: black yellow grey white

The following must be on the billboard:
Logo
phone number: 076 / 913 58 40
website: www.geraetepark-lorvento.ch
the machines I rent out: Bagger bis 10T, Radlader, Dumper, Raupenkipper

the font in the logo is: Square 721

Final format 2950 x 1900mm
I have uploaded pictures:
"Excavator 1-6" are my pictures, which can be used
"Sample 1-4" are pictures whose style I like
"Billboard" are billboards which I like

Requirements
Must have
• The following must be on the billboard: Logo phone number: 076 / 913 58 40 website: www.geraetepark-lorvento.ch the machines I rent out: Bagger bis 10T, Radlader, Dumper, Raupenkipper

```html
<!DOCTYPE html>
<html lang="de">
<head>
<meta charset="utf-8">
<title>Lorvento Gerätepark – Billboard</title>
<link rel="stylesheet" href="https://fonts.googleapis.com/css2?family=Archivo+Black&family=Saira:wght@400;800&display=swap">
<style>
  :root {
    --black: #000000;
    --yellow: #f0cf2e;
    --gold: #e7b70a;
    --white: #ffffff;
    --band: rgba(38, 38, 38, 0.55);
  }
  html, body { margin: 0; padding: 0; background: var(--black); overflow: hidden; }
  .billboard {
    position: relative;
    width: 1200px;
    height: 773px;
    background: var(--black);
    overflow: hidden;
    font-family: "Saira", sans-serif;
  }
  .site-photo {
    position: absolute;
    left: 300px; top: 320px;
    width: 900px; height: 453px;
    background:
      radial-gradient(ellipse 220px 150px at 1110px 230px, rgba(120, 200, 230, 0.55), transparent 70%),
      radial-gradient(ellipse 520px 260px at 620px 330px, rgba(70, 72, 40, 0.75), transparent 75%),
      radial-gradient(ellipse 380px 200px at 300px 380px, rgba(50, 48, 35, 0.6), transparent 80%),
      linear-gradient(180deg, #000 0%, #0d0e0b 45%, #1c1b14 100%);
    -webkit-mask-image: linear-gradient(90deg, transparent 0%, #000 30%);
            mask-image: linear-gradient(90deg, transparent 0%, #000 30%);
  }
  .brand {
    position: absolute;
    left: 57px; top: 62px;
    color: var(--yellow);
    font-family: "Saira", sans-serif;
    font-weight: 800;
    text-transform: uppercase;
    line-height: 1;
  }
  .brand-name { display: block; font-size: 104px; letter-spacing: 4px; }
  .brand-sub { display: block; font-size: 36px; letter-spacing: 14px; margin-top: 8px; }
  .phone {
    position: absolute;
    left: 56px; top: 229px;
    display: flex; align-items: center; gap: 32px;
  }
  .phone-icon { width: 86px; height: 86px; }
  .phone-number {
    color: var(--yellow);
    font-size: 66px;
    font-weight: 400;
    letter-spacing: 5px;
    line-height: 1;
  }
  .rent-label {
    position: absolute;
    left: 57px; top: 348px;
    width: 460px; height: 87px;
    background: var(--white);
    display: flex; align-items: center; justify-content: center;
    font-family: "Archivo Black", sans-serif;
    font-size: 56px;
    color: var(--black);
    letter-spacing: 1px;
  }
  .machine-list {
    position: absolute;
    left: 55px; top: 457px;
    margin: 0; padding: 0;
    list-style: none;
    font-family: "Archivo Black", sans-serif;
    font-size: 48px;
    line-height: 68px;
    letter-spacing: 6px;
    color: var(--gold);
  }
  .web-band {
    position: absolute;
    left: 300px; top: 678px;
    width: 900px; height: 95px;
    background: var(--band);
  }
  .website {
    position: absolute;
    right: 34px; top: 694px;
    color: var(--white);
    font-size: 46px;
    letter-spacing: 5px;
    line-height: 1;
  }
</style>
</head>
<body>
<main class="billboard">
  <div class="site-photo" role="img" aria-label="Night photo of a compact excavator digging, headlights glowing"></div>

  <div class="brand">
    <span class="brand-name">Lorvento</span>
    <span class="brand-sub">Gerätepark</span>
  </div>

  <div class="phone">
    <svg class="phone-icon" viewBox="0 0 86 86" aria-hidden="true">
      <circle cx="43" cy="43" r="41" fill="none" stroke="var(--yellow)" stroke-width="3"/>
      <path d="M30 22 l7 -3 l7 13 l-5 5 c2 6 7 11 13 13 l5 -5 l13 7 l-3 7 c-2 3 -6 4 -10 3 c-14 -4 -26 -16 -30 -30 c-1 -4 0 -8 3 -10 z"
            fill="none" stroke="var(--yellow)" stroke-width="3" stroke-linejoin="round"/>
    </svg>
    <span class="phone-number">076 / 913 58 40</span>
  </div>

  <div class="rent-label">WE RENT OUT</div>

  <ul class="machine-list">
    <li>BAGGER BIS 10T</li>
    <li>RAUPENKIPPER</li>
    <li>RADLADER</li>
    <li>DUMPER</li>
  </ul>

  <div class="web-band"></div>
  <div class="website">www.geraetepark-lorvento.ch</div>
</main>
</body>
</html>
```